Business Card Design Project

Double-side business card.
Side One:
Logo (Including the word TOLVENA that is part of the Logo
"Programas de Cambio Comunitario y Cuidado del Entorno Natural"
Side Two:
Marcela Ontiveros
Co-Founder & CEO
Harlow Bay, ME (USA)
email: marcelao@tolvena.net (please use an icon for "emal")
cell: +1 (202) 384 9170 (please use an icon for "cell")
skype: marceontiv (please use an icon for "skype")
twitter: marceontiv (please use an icon for "twitter")
www.tolvena.net
Target Market(s)
Foundations, Governments, and Private sector companies that implement projects for sustainability.
Industry/Entity Type
Business
Font styles to use
Colors
Designer to choose colors to be used in the design.
Requirements
Nice to have
- barcode

```html
<!DOCTYPE html>
<html lang="es">
<head>
<meta charset="utf-8">
<title>TOLVENA — Business Card</title>
<link rel="stylesheet" href="https://fonts.googleapis.com/css2?family=Fira+Sans:wght@400;600&family=Fira+Sans+Condensed:wght@600&display=swap">
<style>
  :root {
    --bg: #e6e6e6;
    --card: #fbfbfb;
    --red: #cc0a24;
    --ink: #4a4a4a;
    --muted: #6e6e6e;
    --row: #efefef;
    --white: #ffffff;
  }
  * { box-sizing: border-box; margin: 0; padding: 0; }
  html, body {
    width: 1200px; height: 917px; overflow: hidden;
    background: var(--bg);
    font-family: "Fira Sans", sans-serif;
  }
  .sheet {
    position: relative; width: 1200px; height: 917px;
    display: flex; justify-content: center; align-items: center; gap: 70px;
  }
  .card {
    position: relative; width: 440px; height: 770px;
    background: var(--card);
    box-shadow: 0 2px 6px rgba(0,0,0,.12);
    overflow: hidden;
  }

  /* Front */
  .front__band {
    position: absolute; left: 0; right: 0; top: 372px; height: 84px;
    background: var(--red);
    display: flex; align-items: center; justify-content: center;
  }
  .front__name {
    color: var(--white); font-weight: 400; font-size: 64px; letter-spacing: 6px;
  }
  .front__tagline {
    position: absolute; left: 0; right: 0; top: 466px;
    text-align: center; font-size: 12.5px; color: var(--ink);
  }

  /* Back */
  .back__stripe {
    position: absolute; left: 0; top: 40px; width: 48px; height: 470px;
    background: var(--red);
  }
  .back__block {
    position: absolute; left: 0; bottom: 30px; width: 66px; height: 40px;
    background: var(--red);
  }
  .back__name {
    position: absolute; left: 150px; right: 0; top: 60px; height: 42px;
    background: var(--red); color: var(--white);
    font-family: "Fira Sans Condensed", sans-serif; font-weight: 600; font-size: 26px;
    padding-left: 14px; line-height: 42px;
  }
  .back__title {
    position: absolute; left: 164px; top: 108px;
    font-size: 18px; color: var(--ink);
  }
  .back__brand {
    position: absolute; left: 164px; top: 190px;
    font-size: 34px; font-weight: 400; letter-spacing: 3px; color: var(--muted);
  }
  .contacts {
    position: absolute; left: 150px; right: 18px; top: 252px;
    list-style: none;
  }
  .contacts__item {
    display: flex; align-items: center; gap: 16px;
    height: 38px; margin-bottom: 6px; padding-left: 18px;
    background: var(--row);
    font-size: 17px; color: var(--ink);
    white-space: nowrap;
  }
  .contacts__item:nth-child(even) { background: transparent; }
  .contacts__icon { width: 16px; height: 16px; flex: none; }
</style>
</head>
<body>
<main class="sheet">

  <section class="card front" aria-label="Frente de la tarjeta">
    <div class="front__band"><span class="front__name">TOLVENA</span></div>
    <p class="front__tagline">“Programas de Cambio Comunitario y Cuidado del Entorno Natural”</p>
  </section>

  <section class="card back" aria-label="Reverso de la tarjeta">
    <div class="back__stripe"></div>
    <div class="back__block"></div>
    <h1 class="back__name">Marcela Ontiveros</h1>
    <p class="back__title">Co-Founder &amp; CEO</p>
    <p class="back__brand">TOLVENA</p>
    <ul class="contacts">
      <li class="contacts__item">
        <svg class="contacts__icon" viewBox="0 0 16 16" aria-hidden="true"><path d="M8 1a5 5 0 0 0-5 5c0 4 5 9 5 9s5-5 5-9a5 5 0 0 0-5-5zm0 7a2 2 0 1 1 0-4 2 2 0 0 1 0 4z" fill="var(--red)"/></svg>
        Harlow Bay, ME (USA)
      </li>
      <li class="contacts__item">
        <svg class="contacts__icon" viewBox="0 0 16 16" aria-hidden="true"><path d="M4 1l3 3-1.5 2a8 8 0 0 0 4.5 4.5L12 9l3 3-2 2.5C7 14 2 9 1.5 3z" fill="var(--red)"/></svg>
        +1 (202) 384 9170
      </li>
      <li class="contacts__item">
        <svg class="contacts__icon" viewBox="0 0 16 16" aria-hidden="true"><rect x="1" y="3" width="14" height="10" fill="none" stroke="var(--red)" stroke-width="1.6"/><path d="M1 3l7 6 7-6" fill="none" stroke="var(--red)" stroke-width="1.6"/></svg>
        marcelao@tolvena.net
      </li>
      <li class="contacts__item">
        <svg class="contacts__icon" viewBox="0 0 16 16" aria-hidden="true"><circle cx="8" cy="8" r="6.5" fill="none" stroke="var(--red)" stroke-width="1.5"/><ellipse cx="8" cy="8" rx="3" ry="6.5" fill="none" stroke="var(--red)" stroke-width="1.2"/><path d="M1.5 8h13" stroke="var(--red)" stroke-width="1.2"/></svg>
        www.tolvena.net
      </li>
      <li class="contacts__item">
        <svg class="contacts__icon" viewBox="0 0 16 16" aria-hidden="true"><circle cx="8" cy="8" r="6" fill="var(--red)"/></svg>
        marceontiv
      </li>
      <li class="contacts__item">
        <svg class="contacts__icon" viewBox="0 0 16 16" aria-hidden="true"><rect x="2" y="2" width="12" height="12" fill="var(--red)"/></svg>
        marceontiv
      </li>
    </ul>
  </section>

</main>
</body>
</html>
```